Poster/Banner design for Hockey Skating business with the theme SPEED

We need 1 large banner and 2 posters (on stands) created for inside Arena advertising. We want to use the attached Fleet Hollow (FH) example as a guide for this design request. The theme is Speed. We want to see a mature hockey player skating very fast in a forward stride position. We want to see elements of speed from the hockey player and also from its surroundings like the FH example with the landscape blurred from the speed. Our logo is to be prominent in the poster. The message; Skate Fast. Be First (or 1st). THINK SPEED. website address & social media icons also to be included
Updates

Target Market(s)

Hockey Dads; age 35- 55 yrs, affluent, competitive

Colors

Designer to choose colors to be used in the design.

Requirements
Must have
• - 2 posters to go in 1 poster stand; the message/image theme is to be similar to the banner - approx 22" x 28" (specification enclosed in a word document)
• - 1 large banner - approx 48" x 79" (specification enclosed in a word document)
• - all elements in vector graphics; -CYMK colors (and Pantone colors if possible); min. 300 dpi

```html
<!DOCTYPE html>
<html lang="en">
<head>
<meta charset="utf-8">
<title>Stride Line Skating – Think Speed Banner</title>
<link rel="stylesheet" href="https://fonts.googleapis.com/css2?family=Exo+2:ital,wght@0,700;0,900;1,900&family=Montserrat:wght@600;700&display=swap">
<style>
  :root {
    --brand-red: #d71f2d;
    --deep-red: #8e1019;
    --ink: #111111;
    --paper: #ffffff;
    --ice-light: #e1e6e4;
    --ice-mid: #b9bfbd;
    --rink-dark: #5d605e;
    --jersey-light: #bfe6f4;
    --jersey-mid: #7cc4e2;
    --pants-navy: #1e2c4a;
    --social-a: #4a90d9;
    --social-b: #d72b2b;
    --social-c: #c13584;
    --social-d: #3b5998;
  }
  * { box-sizing: border-box; margin: 0; padding: 0; }
  html, body { width: 759px; height: 1200px; overflow: hidden; background: var(--paper); }
  .banner { position: relative; width: 759px; height: 1200px; overflow: hidden; background: var(--paper); font-family: "Exo 2", sans-serif; }

  .rink-backdrop {
    position: absolute; left: 0; top: 0; width: 759px; height: 960px;
    background: linear-gradient(180deg, var(--ice-mid) 0%, var(--ice-light) 28%, #c4c9c7 46%, var(--rink-dark) 58%, #8d908e 70%, var(--ice-light) 84%, var(--ice-light) 100%);
  }

  .player-photo {
    position: absolute; left: 110px; top: 240px; width: 540px; height: 590px;
    border-radius: 40px;
    background: linear-gradient(180deg, var(--jersey-light) 0%, var(--jersey-mid) 45%, var(--pants-navy) 62%, var(--jersey-mid) 80%, #9fb7c2 100%);
  }

  .brand-mark {
    position: absolute; left: 0; top: 62px; width: 759px; text-align: center;
    font-weight: 900; font-size: 44px; line-height: 1; letter-spacing: 1px;
    color: var(--brand-red); text-transform: uppercase;
  }
  .tagline { position: absolute; left: 200px; top: 150px; width: 360px; height: 70px; }
  .tagline text { font-family: "Exo 2", sans-serif; font-weight: 700; font-size: 23px; fill: var(--ink); }

  .headline { position: absolute; width: 759px; left: 0; text-align: center; font-weight: 900; font-style: italic; text-transform: uppercase; line-height: 1; letter-spacing: -1px; }
  .headline--skate { top: 800px; font-size: 72px; color: var(--brand-red); padding-left: 20px; }
  .headline--first { top: 878px; font-size: 72px; color: var(--ink); padding-left: 20px; }

  .speed-band { position: absolute; left: 0; top: 950px; width: 759px; height: 172px; }
  .speed-title {
    position: absolute; left: 0; top: 992px; width: 759px; text-align: center;
    font-weight: 900; font-style: italic; font-size: 96px; line-height: 1;
    color: var(--paper); text-shadow: 4px 4px 0 var(--deep-red); letter-spacing: -1px;
  }

  .contact { position: absolute; left: 14px; top: 1136px; font-family: "Montserrat", sans-serif; color: var(--ink); }
  .contact-lead { font-size: 11px; font-weight: 600; }
  .contact-url { font-size: 19px; font-weight: 700; margin-top: 2px; }

  .social-list { position: absolute; right: 14px; top: 1144px; display: flex; gap: 10px; list-style: none; font-family: "Montserrat", sans-serif; }
  .social-item { display: flex; align-items: center; gap: 4px; font-size: 11px; font-weight: 700; color: var(--ink); }
  .social-dot { width: 28px; height: 28px; border-radius: 50%; display: inline-block; }
  .social-dot--a { background: var(--social-a); }
  .social-dot--b { background: var(--social-b); }
  .social-dot--c { background: var(--social-c); }
  .social-dot--d { background: var(--social-d); }
</style>
</head>
<body>
<main class="banner">
  <div class="rink-backdrop" role="img" aria-label="Arena and ice surface blurred by motion streaks"></div>
  <div class="player-photo" role="img" aria-label="Photo of a mature hockey player in a light blue jersey and navy pants skating fast toward the viewer in a forward stride, stick in hand"></div>

  <div class="brand-mark">Stride Line Skating</div>
  <svg class="tagline" viewBox="0 0 360 70" aria-label="Give your player the edge">
    <defs><path id="tagline-arc" d="M10 22 Q180 62 350 22"/></defs>
    <text><textPath href="#tagline-arc" startOffset="50%" text-anchor="middle">Give your player the edge</textPath></text>
  </svg>

  <h1 class="headline headline--skate">Skate Fast</h1>
  <h2 class="headline headline--first">Be First</h2>

  <svg class="speed-band" viewBox="0 0 759 172" preserveAspectRatio="none" aria-hidden="true">
    <path fill="var(--brand-red)" d="M0 12 L40 8 L80 11 L130 6 L190 10 L250 5 L310 9 L370 4 L430 8 L490 5 L550 9 L610 6 L670 10 L720 7 L759 9 L759 152 L720 156 L680 152 L630 158 L580 153 L530 159 L470 154 L410 160 L350 155 L290 161 L230 156 L170 162 L110 157 L60 163 L20 158 L0 160 Z"/>
  </svg>
  <div class="speed-title">THINK SPEED</div>

  <div class="contact">
    <p class="contact-lead">to learn more about us:</p>
    <p class="contact-url">www.stridelineskating.com</p>
  </div>

  <ul class="social-list">
    <li class="social-item"><span class="social-dot social-dot--a"></span>Chirpa</li>
    <li class="social-item"><span class="social-dot social-dot--b"></span>Reelo</li>
    <li class="social-item"><span class="social-dot social-dot--c"></span>Lenso</li>
    <li class="social-item"><span class="social-dot social-dot--d"></span>Circlo</li>
  </ul>
</main>
</body>
</html>
```